2 Stellenanzeigenbanner für Personaldienstleister zur Werbung auf Promotion-Jobplattform
Die Qualität der Arbeiten war sehr gut. Die Kommunikation mit dem Designer klappte hervorragend. Wir können eine Zusammenarbeit absolut empfehlen!
Zielgruppe
Unser Unternehmen ist primär im Bereich der personalgestützten Absatzförderung am Point of Sale (PoS) mit Schwerpunkt Sales Promotion tätig. Die Zielgruppe der Banner als einzusetzende Werbemittel besteht in erster Linie aus Freiberuflern aus den Bereichen Verkauf und Promotion, die als Markenbotschafter und Fachberater im Auftrag unserer Kunden an den Verkaufspunkten agieren.
Aufgabenstellung
Zur Veröffentlichung auf einer bekannten Promotion-Jobplattform müssen 2 statische Banner in den Formaten 1) 160 x 600 und 2) 468 x 60 erstellt werden, die zu einer Stellenausschreibung führen. Die Banner müssen das offizielle Logo der Agentur sowie die Unternehmensfarben (Rot & Blau) beinhalten und gemeinsam ein einheitliches Design bilden. Die zu verwendenden Textinhalte finden sich in den Anhängen "Text 1" und "Text 2", können vom Designer aber frei angepasst werden.

```html
<!DOCTYPE html>
<html lang="de">
<head>
<meta charset="utf-8">
<title>Stellenanzeigenbanner – Tempokraft</title>
<link rel="stylesheet" href="https://fonts.googleapis.com/css2?family=Open+Sans:wght@300;400;600;700&display=swap">
<style>
  :root {
    --brand-blue: #0b4b73;
    --brand-red: #95102f;
    --canvas: #ffffff;
    --text-light: #ffffff;
    --frame: #e3e3e3;
    --sky-top: #a9a290;
    --sky-mid: #8f9594;
    --lake: #a7b1b3;
    --hills: #5c6354;
    --ground: #4d4f45;
    --shirt: #e9e2d8;
    --trousers: #3b3d42;
    --denim: #6f88a8;
  }
  * { box-sizing: border-box; margin: 0; padding: 0; }
  html, body { width: 1200px; height: 788px; overflow: hidden; background: var(--canvas); }
  body { position: relative; font-family: "Open Sans", Arial, sans-serif; }

  /* Skyscraper 160 x 600 */
  .skyscraper {
    position: absolute; top: 97px; width: 154px; height: 580px;
    border: 1px solid var(--frame); overflow: hidden; background: var(--canvas);
  }
  .skyscraper--man { left: 67px; }
  .skyscraper--woman { left: 251px; }
  .skyscraper--duo { left: 435px; }

  .skyscraper__photo {
    position: absolute; left: 0; top: 40px; width: 100%; height: 510px;
    background: linear-gradient(180deg,
      var(--sky-top) 0%, #9d9a8a 25%, #8c8f88 45%,
      var(--hills) 53%, var(--lake) 55%, #97a2a4 62%,
      #5d6a4e 68%, var(--ground) 80%, #6d6e68 88%, #ffffff 100%);
  }
  .skyscraper__runner {
    position: absolute; top: 185px; height: 275px;
    border-radius: 48% 48% 40% 40%;
  }
  .skyscraper--man .skyscraper__runner {
    left: 8px; width: 140px;
    background: linear-gradient(180deg, rgba(233,226,216,.0) 0%, var(--shirt) 22%, #d8d1c6 48%, var(--trousers) 60%, #2e3034 90%, rgba(46,48,52,0) 100%);
  }
  .skyscraper--woman .skyscraper__runner {
    left: 6px; width: 144px;
    background: linear-gradient(180deg, rgba(232,221,222,0) 0%, #e8dcdc 22%, #d9cccc 48%, var(--denim) 60%, #5a7290 90%, rgba(90,114,144,0) 100%);
  }
  .skyscraper--duo .skyscraper__runner {
    left: 2px; width: 150px;
    background: linear-gradient(180deg, rgba(233,226,216,0) 0%, var(--shirt) 22%, #ddd4cc 48%, #4a5566 60%, #3d4656 90%, rgba(61,70,86,0) 100%);
  }
  .skyscraper__header { position: absolute; left: 0; top: 0; width: 100%; height: 74px; }
  .skyscraper__header-text {
    position: absolute; left: 0; top: 13px; width: 100%;
    text-align: center; color: var(--text-light);
    font-weight: 700; font-size: 15px; line-height: 19px;
  }
  .skyscraper__headline {
    position: absolute; left: 0; top: 86px; width: 100%;
    text-align: center; color: var(--text-light);
    font-weight: 400; font-size: 17px; line-height: 24px; letter-spacing: .3px;
  }
  .skyscraper__cta { position: absolute; left: 0; top: 416px; width: 152px; height: 108px; }
  .skyscraper__cta-text {
    position: absolute; left: 9px; top: 453px; color: var(--text-light);
    font-weight: 700; line-height: 1; transform: rotate(-4deg); transform-origin: left top;
  }
  .skyscraper__cta-small { display: block; font-size: 13.5px; letter-spacing: .2px; }
  .skyscraper__cta-large { display: block; font-size: 21px; margin-top: 2px; }
  .skyscraper__brand {
    position: absolute; left: 0; top: 545px; width: 100%; text-align: center;
  }
  .brand-name { color: var(--brand-blue); font-weight: 700; }
  .skyscraper__brand .brand-name { font-size: 15px; line-height: 16px; display: inline-flex; align-items: center; gap: 5px; }
  .brand-dot { width: 7px; height: 7px; border-radius: 50%; background: var(--brand-red); display: inline-block; }
  .skyscraper__tagline {
    display: block; margin-top: 3px; color: var(--brand-red);
    font-size: 6px; line-height: 8px; font-weight: 600; letter-spacing: 1.6px;
  }

  /* Leaderboard 468 x 60 */
  .leaderboard {
    position: absolute; left: 658px; width: 452px; height: 58px;
    border: 1px solid var(--frame); overflow: hidden; background: var(--canvas);
  }
  .leaderboard--woman { top: 97px; }
  .leaderboard--man { top: 184px; }
  .leaderboard--duo { top: 271px; }
  .leaderboard__photo {
    position: absolute; left: 60px; top: 0; width: 290px; height: 100%;
    background: linear-gradient(90deg, #8d8a7c 0%, #9b9a8e 40%, #a9aba4 72%, #ffffff 100%);
  }
  .leaderboard__runner {
    position: absolute; left: 200px; top: 2px; width: 58px; height: 54px;
    border-radius: 45%;
    background: radial-gradient(ellipse at 50% 40%, var(--shirt) 0%, #cfc8bd 45%, rgba(160,160,150,0) 75%);
  }
  .leaderboard__badge { position: absolute; left: 0; top: 0; width: 74px; height: 58px; }
  .leaderboard__badge-text {
    position: absolute; left: 0; top: 8px; width: 66px; text-align: center;
    color: var(--text-light); font-weight: 700; font-size: 11.5px; line-height: 14px;
  }
  .leaderboard__headline {
    position: absolute; left: 80px; top: 7px; color: var(--text-light);
    font-weight: 600; font-size: 12.5px; line-height: 13.5px; letter-spacing: .3px;
  }
  .leaderboard__cta { position: absolute; left: 256px; top: 0; width: 103px; height: 58px; }
  .leaderboard__cta-text {
    position: absolute; left: 264px; top: 15px; color: var(--text-light);
    font-weight: 700; line-height: 1; transform: rotate(-3deg); transform-origin: left top;
  }
  .leaderboard__cta-small { display: block; font-size: 9.5px; }
  .leaderboard__cta-large { display: block; font-size: 14px; margin-top: 2px; }
  .leaderboard__brand {
    position: absolute; left: 360px; top: 0; width: 91px; height: 58px;
    display: flex; flex-direction: column; align-items: center; justify-content: center; gap: 3px;
  }
  .leaderboard__brand .brand-name { font-size: 13px; line-height: 14px; }
</style>
</head>
<body>

<section class="skyscraper skyscraper--man">
  <div class="skyscraper__photo" role="img" aria-label="Foto: Seelandschaft mit bewölktem Himmel"></div>
  <div class="skyscraper__runner" role="img" aria-label="Foto: Mann im Hemd sprintet nach rechts"></div>
  <svg class="skyscraper__header" viewBox="0 0 154 74" aria-hidden="true"><polygon points="0,0 154,0 154,49 77,74 0,49" fill="var(--brand-blue)"/></svg>
  <p class="skyscraper__header-text">WIR SUCHEN<br>DICH!</p>
  <h2 class="skyscraper__headline">SALES<br>PROMOTER &amp;<br>FACHBERATER<br>AUFGEPASST!</h2>
  <svg class="skyscraper__cta" viewBox="0 0 152 108" aria-hidden="true"><polygon points="0,33 105,24 105,0 152,48 108,108 106,84 0,92" fill="var(--brand-red)"/></svg>
  <p class="skyscraper__cta-text"><span class="skyscraper__cta-small">JETZT SCHNELL</span><span class="skyscraper__cta-large">BEWERBEN</span></p>
  <div class="skyscraper__brand"><span class="brand-name"><i class="brand-dot"></i>Tempokraft</span><span class="skyscraper__tagline">PERSONAL FÜR DEN HANDEL</span></div>
</section>

<section class="skyscraper skyscraper--woman">
  <div class="skyscraper__photo" role="img" aria-label="Foto: Seelandschaft mit bewölktem Himmel"></div>
  <div class="skyscraper__runner" role="img" aria-label="Foto: Frau in Bluse und Jeans sprintet nach rechts"></div>
  <svg class="skyscraper__header" viewBox="0 0 154 74" aria-hidden="true"><polygon points="0,0 154,0 154,49 77,74 0,49" fill="var(--brand-blue)"/></svg>
  <p class="skyscraper__header-text">WIR SUCHEN<br>DICH!</p>
  <h2 class="skyscraper__headline">SALES<br>PROMOTER &amp;<br>FACHBERATER<br>AUFGEPASST!</h2>
  <svg class="skyscraper__cta" viewBox="0 0 152 108" aria-hidden="true"><polygon points="0,33 105,24 105,0 152,48 108,108 106,84 0,92" fill="var(--brand-red)"/></svg>
  <p class="skyscraper__cta-text"><span class="skyscraper__cta-small">JETZT SCHNELL</span><span class="skyscraper__cta-large">BEWERBEN</span></p>
  <div class="skyscraper__brand"><span class="brand-name"><i class="brand-dot"></i>Tempokraft</span><span class="skyscraper__tagline">PERSONAL FÜR DEN HANDEL</span></div>
</section>

<section class="skyscraper skyscraper--duo">
  <div class="skyscraper__photo" role="img" aria-label="Foto: Seelandschaft mit bewölktem Himmel"></div>
  <div class="skyscraper__runner" role="img" aria-label="Foto: Mann und Frau sprinten nebeneinander nach rechts"></div>
  <svg class="skyscraper__header" viewBox="0 0 154 74" aria-hidden="true"><polygon points="0,0 154,0 154,49 77,74 0,49" fill="var(--brand-blue)"/></svg>
  <p class="skyscraper__header-text">WIR SUCHEN<br>DICH!</p>
  <h2 class="skyscraper__headline">SALES<br>PROMOTER &amp;<br>FACHBERATER<br>AUFGEPASST!</h2>
  <svg class="skyscraper__cta" viewBox="0 0 152 108" aria-hidden="true"><polygon points="0,33 105,24 105,0 152,48 108,108 106,84 0,92" fill="var(--brand-red)"/></svg>
  <p class="skyscraper__cta-text"><span class="skyscraper__cta-small">JETZT SCHNELL</span><span class="skyscraper__cta-large">BEWERBEN</span></p>
  <div class="skyscraper__brand"><span class="brand-name"><i class="brand-dot"></i>Tempokraft</span><span class="skyscraper__tagline">PERSONAL FÜR DEN HANDEL</span></div>
</section>

<section class="leaderboard leaderboard--woman">
  <div class="leaderboard__photo" role="img" aria-label="Foto: Seelandschaft"></div>
  <div class="leaderboard__runner" role="img" aria-label="Foto: sprintende Frau"></div>
  <svg class="leaderboard__badge" viewBox="0 0 74 58" aria-hidden="true"><polygon points="0,0 66,0 74,29 66,58 0,58" fill="var(--brand-blue)"/></svg>
  <p class="leaderboard__badge-text">WIR<br>SUCHEN<br>DICH</p>
  <h2 class="leaderboard__headline">SALES PROMOTER<br>&amp; FACHBERATER<br>AUFGEPASST!</h2>
  <svg class="leaderboard__cta" viewBox="0 0 103 58" aria-hidden="true"><polygon points="0,9 80,5 80,0 103,29 81,58 81,50 0,51" fill="var(--brand-red)"/></svg>
  <p class="leaderboard__cta-text"><span class="leaderboard__cta-small">JETZT SCHNELL</span><span class="leaderboard__cta-large">BEWERBEN</span></p>
  <div class="leaderboard__brand"><i class="brand-dot"></i><span class="brand-name">Tempokraft</span></div>
</section>

<section class="leaderboard leaderboard--man">
  <div class="leaderboard__photo" role="img" aria-label="Foto: Seelandschaft"></div>
  <div class="leaderboard__runner" role="img" aria-label="Foto: sprintender Mann"></div>
  <svg class="leaderboard__badge" viewBox="0 0 74 58" aria-hidden="true"><polygon points="0,0 66,0 74,29 66,58 0,58" fill="var(--brand-blue)"/></svg>
  <p class="leaderboard__badge-text">WIR<br>SUCHEN<br>DICH</p>
  <h2 class="leaderboard__headline">SALES PROMOTER<br>&amp; FACHBERATER<br>AUFGEPASST!</h2>
  <svg class="leaderboard__cta" viewBox="0 0 103 58" aria-hidden="true"><polygon points="0,9 80,5 80,0 103,29 81,58 81,50 0,51" fill="var(--brand-red)"/></svg>
  <p class="leaderboard__cta-text"><span class="leaderboard__cta-small">JETZT SCHNELL</span><span class="leaderboard__cta-large">BEWERBEN</span></p>
  <div class="leaderboard__brand"><i class="brand-dot"></i><span class="brand-name">Tempokraft</span></div>
</section>

<section class="leaderboard leaderboard--duo">
  <div class="leaderboard__photo" role="img" aria-label="Foto: Seelandschaft"></div>
  <div class="leaderboard__runner" role="img" aria-label="Foto: Mann und Frau sprinten"></div>
  <svg class="leaderboard__badge" viewBox="0 0 74 58" aria-hidden="true"><polygon points="0,0 66,0 74,29 66,58 0,58" fill="var(--brand-blue)"/></svg>
  <p class="leaderboard__badge-text">WIR<br>SUCHEN<br>DICH</p>
  <h2 class="leaderboard__headline">SALES PROMOTER<br>&amp; FACHBERATER<br>AUFGEPASST!</h2>
  <svg class="leaderboard__cta" viewBox="0 0 103 58" aria-hidden="true"><polygon points="0,9 80,5 80,0 103,29 81,58 81,50 0,51" fill="var(--brand-red)"/></svg>
  <p class="leaderboard__cta-text"><span class="leaderboard__cta-small">JETZT SCHNELL</span><span class="leaderboard__cta-large">BEWERBEN</span></p>
  <div class="leaderboard__brand"><i class="brand-dot"></i><span class="brand-name">Tempokraft</span></div>
</section>

</body>
</html>
```